New Business Card Design Project

New business card design required for an electrical business in Australia. Offering quality electrical services including design and installation. Electrical services offered are domestic, commercial and industrial. Also meets all the air conditioning installation and maintenance needs.

Target Market(s)

The business is sleek, professional and caters primarily to wealthy clients and government contracts looking for exceptional, tailored service.

Industry/Entity Type

Electrical

Contact Information for Business Card

Gareth Pollwick (Director)
0438 692 174
admin@rvoelectrical.com.au
www.rvoelectrical.com.au

Font styles to use
Sans Serif

Requirements
Must have
• The business card must show the license number - 64139 to comply with legislation.
Nice to have
• The logo colours and fonts could be incorporated into the design if the designer sees fit. We are open to new ideas and welcome creativity. The logo style guide is attached for reference if required.

```html
<!DOCTYPE html>
<html lang="en">
<head>
<meta charset="UTF-8">
<title>RVO Electrical – Business Card</title>
<link href="https://fonts.googleapis.com/css2?family=Roboto:wght@300;400;500;700&display=swap" rel="stylesheet">
<style>
  :root {
    --navy-deep: #0f2349;
    --navy: #1a3466;
    --navy-light: #2a4a85;
    --white: #ffffff;
    --ink: #1c2f55;
    --line: rgba(255,255,255,0.55);
    --stage: #e6e8ec;
  }
  * { margin: 0; padding: 0; box-sizing: border-box; }
  html, body {
    width: 1200px; height: 900px; overflow: hidden;
    background: var(--stage);
    font-family: "Roboto", Arial, sans-serif;
  }
  .sheet {
    width: 1200px; height: 900px;
    display: flex; flex-direction: column;
    align-items: center; justify-content: center; gap: 40px;
  }
  .card {
    position: relative;
    width: 660px; height: 400px;
    border-radius: 22px;
    overflow: hidden;
    background: linear-gradient(135deg, var(--navy-light) 0%, var(--navy) 45%, var(--navy-deep) 100%);
    box-shadow: 0 10px 30px rgba(15,35,73,0.25);
    color: var(--white);
  }

  /* back */
  .card-back .brand {
    position: absolute; left: 0; right: 0; top: 50%;
    transform: translateY(-50%);
    text-align: center;
    font-weight: 500; font-size: 60px; letter-spacing: 4px;
    color: #284478;
  }

  /* front */
  .brand-front {
    position: absolute; left: 40px; top: 96px;
    display: flex; align-items: center; gap: 12px;
    font-weight: 500; font-size: 40px; letter-spacing: 3px;
    line-height: 48px;
    color: var(--white);
  }
  .brand-front .dot {
    width: 12px; height: 12px; border-radius: 50%;
    background: var(--white);
  }
  .bulbs {
    position: absolute; right: 40px; top: 0;
    width: 230px; height: 140px;
    background: linear-gradient(180deg, rgba(255,255,255,0.02), rgba(255,255,255,0.10));
    border-radius: 0 0 10px 10px;
  }
  .rule { position: absolute; height: 1px; background: var(--line); }
  .rule-top { right: 30px; top: 166px; width: 400px; }
  .rule-contact { left: 40px; top: 262px; width: 320px; }

  .person {
    position: absolute; right: 36px; top: 174px; text-align: right;
  }
  .person .name {
    font-weight: 700; font-size: 28px; letter-spacing: 0.5px;
    text-transform: uppercase; line-height: 34px;
  }
  .person .role { font-weight: 400; font-size: 17px; margin-top: 2px; }

  .contacts {
    position: absolute; left: 40px; top: 272px;
    list-style: none;
  }
  .contacts li {
    display: flex; align-items: center; gap: 12px;
    font-size: 19px; font-weight: 400; line-height: 27px;
  }
  .contacts svg { width: 17px; height: 17px; flex: none; }

  .band { position: absolute; left: 0; top: 0; width: 660px; height: 400px; pointer-events: none; }
  .license {
    position: absolute; right: 36px; top: 332px;
    font-size: 17px; line-height: 22px; color: var(--ink); font-weight: 400;
  }
</style>
</head>
<body>
<main class="sheet">

  <section class="card card-back" aria-label="Card back">
    <div class="brand">RVO ELECTRICAL</div>
  </section>

  <section class="card card-front" aria-label="Card front">
    <div class="bulbs" role="img" aria-label="Line illustration of light bulbs hanging on cords"></div>

    <div class="brand-front"><span>RVO ELECTRICAL</span><span class="dot"></span></div>

    <div class="rule rule-top"></div>
    <div class="person">
      <div class="name">Gareth Pollwick</div>
      <div class="role">Director</div>
    </div>

    <div class="rule rule-contact"></div>
    <ul class="contacts">
      <li>
        <svg viewBox="0 0 24 24" fill="none" stroke="#fff" stroke-width="2"><path d="M5 3h4l2 5-2.5 1.5a11 11 0 0 0 6 6L16 13l5 2v4a2 2 0 0 1-2 2A16 16 0 0 1 3 5a2 2 0 0 1 2-2z"/></svg>
        <span>0438 692 174</span>
      </li>
      <li>
        <svg viewBox="0 0 24 24" fill="none" stroke="#fff" stroke-width="2"><rect x="3" y="5" width="18" height="14" rx="1"/><path d="M3 6l9 7 9-7"/></svg>
        <span>admin@rvoelectrical.com.au</span>
      </li>
      <li>
        <svg viewBox="0 0 24 24" fill="none" stroke="#fff" stroke-width="2"><circle cx="12" cy="12" r="9"/><path d="M3 12h18M12 3a14 14 0 0 1 0 18M12 3a14 14 0 0 0 0 18"/></svg>
        <span>www.rvoelectrical.com.au</span>
      </li>
    </ul>

    <svg class="band" viewBox="0 0 660 400" aria-hidden="true">
      <rect x="0" y="372" width="660" height="28" fill="#ffffff"/>
      <polygon points="405,372 430,312 660,312 660,372" fill="#ffffff"/>
      <polygon points="378,372 401,318 413,318 390,372" fill="#ffffff"/>
    </svg>
    <div class="license">license number - 64139</div>
  </section>

</main>
</body>
</html>
```